Healthy Products Company Needs to Refresh Their Web Image

This is a web relaunch for a company that creates a nutritional supplement made out of Greenlipped Mussels that are native to and grow only in New Zealand. This product is a health superfood which is excellent support for many conditions such as arthritis, heart disease, joint mobility, and healthy lung function, etc. Tovrel Aquaculture is a pioneer in this industry having started in 1967. They have pioneered and are the only company in the business to use cool drying methodology to dry their mussels. This low heat process doesn't degrade nutritional and health giving properties of the mussels. The final design should communicate, cool, healthy, green and natural feeling superimposed on cutting edge technology, and pharmaceutical purity. Natural yet scientific. Also a certain solidity and trustworthiness.
Updates

Hi: The web site name is www.tovrel.com and I would like to have both the psd file and the underlying code.
Thank you.

Target Market(s)

Corporates: Pharmaceutical Companies, Heath Product Companies

Industry/Entity Type

Pharmaceutical

Requirements
Must have
• Currently we have no way to order the product online and we will not be doing this in the current site. However, capability to do that in the future would be nice.
Please see the previous web site for understanding of what the company does. Plese feel free to run with any ideas you may have in layout or content. I have enclosed a new logo for the company. Please make sure you carry the style of the logo throughout the new web site. I don't have any new pictures we can use right now but I will include a background picture you can use for now as a placeholder.

```html
<!DOCTYPE html>
<html lang="en">
<head>
<meta charset="utf-8">
<title>Tovrel Aquaculture Ltd</title>
<link href="https://fonts.googleapis.com/css2?family=Rokkitt:wght@400;700&family=Roboto+Condensed:wght@400;700&family=PT+Sans:wght@400&family=Arimo:wght@400;700&display=swap" rel="stylesheet">
<style>
:root{
  --blue:#1a73bf;
  --blue-dark:#0d5ea8;
  --green:#0a8a3f;
  --green-dark:#067334;
  --text-dark:#333;
  --footer-bg:#262626;
  --footer-bar:#1d1d1d;
  --footer-text:#c9c9c9;
  --footer-head:#16a34a;
}
*{margin:0;padding:0;box-sizing:border-box}
html,body{width:1200px;height:1200px;overflow:hidden}
body{position:relative;background:#fff;font-family:"PT Sans",sans-serif}
.abs{position:absolute}
.logo{left:106px;top:24px;display:flex;align-items:center;gap:12px;white-space:nowrap}
.logo-dot{width:54px;height:54px;border-radius:50%;background:var(--green)}
.logo-name{font-family:"Rokkitt",serif;font-size:40px;color:var(--blue);font-weight:400;letter-spacing:-.3px}
.contact{right:115px;top:30px;width:330px;text-align:right;font-family:"Arimo",sans-serif;white-space:nowrap}
.contact-top{font-size:13px;font-weight:700;color:var(--text-dark);padding-bottom:6px;border-bottom:1px dotted #888}
.contact-top b{color:var(--blue);font-size:15px}
.contact-call{display:flex;justify-content:flex-end;align-items:center;gap:6px;padding:5px 0 6px;border-bottom:1px dotted #888;font-family:"Roboto Condensed",sans-serif;font-size:19px;color:#222;white-space:nowrap}
.contact-call .label{letter-spacing:-.2px}
.contact-call .num{color:var(--blue);font-size:26px;line-height:1;margin-left:4px}
.phone-ico{width:30px;height:30px;flex:none;background:var(--green);border-radius:3px;display:flex;align-items:center;justify-content:center;margin-right:2px}
.hero{left:0;top:150px;width:1200px;height:465px;background:linear-gradient(180deg,#cdeff7 0%,#5fd8ee 12%,#3b78c9 25%,#1f5a3a 55%,#0f3a1f 80%,#2b7f9e 100%)}
.arrow{top:312px}
.nav{left:106px;top:118px;width:987px;height:47px;background:linear-gradient(#1d86d3,#0e61b0);border-radius:3px;display:flex;align-items:center;font-family:"Roboto Condensed",sans-serif;font-weight:700;font-size:15px;color:#fff;white-space:nowrap}
.nav a{color:#fff;text-decoration:none;text-shadow:0 1px 1px rgba(0,0,0,.4);height:47px;display:flex;align-items:center;justify-content:center;border-right:1px solid rgba(255,255,255,.15)}
.nav a:last-child{border:none}
.nav .home{margin-left:16px;width:85px;height:52px;align-self:flex-start;background:linear-gradient(#0d9a45,#06753a);border-radius:0 0 6px 6px}
.below{left:0;top:615px;width:1200px;height:272px;background:linear-gradient(#d9d9d9,#f4f4f4 60%,#fafafa)}
.intro{left:118px;top:538px;width:967px;height:263px;background:linear-gradient(#0d9346,#067a36);border:1px solid #0b6c31;border-radius:8px;color:#fff;text-align:center}
.intro h1{font-family:"Rokkitt",serif;font-weight:400;font-size:46px;letter-spacing:2px;margin-top:18px;padding-bottom:8px;border-bottom:1px solid rgba(255,255,255,.15);margin-left:180px;margin-right:180px;white-space:nowrap}
.intro p{font-size:16px;line-height:22px;margin:14px 28px 0}
.more{left:462px;top:773px;width:279px;height:50px;border-radius:12px;background:linear-gradient(#f8f8f8,#cfcfcf);box-shadow:0 4px 6px rgba(0,0,0,.3);font-family:"Arimo",sans-serif;font-size:23px;color:#333;display:flex;align-items:center;justify-content:center;gap:14px;white-space:nowrap}
.footer{left:0;top:887px;width:1200px;height:255px;background:var(--footer-bg)}
.foot-col h3{font-family:"Rokkitt",serif;font-weight:700;font-size:22px;color:var(--footer-head);letter-spacing:.5px;margin-bottom:14px}
.foot-col li{list-style:none;font-family:"Arimo",sans-serif;font-size:12.5px;color:var(--footer-text);letter-spacing:.6px;height:24px;display:flex;align-items:center;gap:6px;white-space:nowrap}
.foot-col li::before{content:"»";color:#2a8de0;font-size:16px;line-height:1}
.map{left:750px;top:904px;width:318px;height:224px;border:3px solid #555;background:linear-gradient(90deg,#8fb86a 0%,#b6d08a 45%,#a8c0f5 60%,#a8c0f5 100%)}
.bottom{left:0;top:1142px;width:1200px;height:58px;background:var(--footer-bar);border-top:1px solid #3a3a3a;display:flex;justify-content:center;align-items:center;gap:14px;font-family:"Arimo",sans-serif;font-size:12.5px;color:#aaa;letter-spacing:.8px;white-space:nowrap}
</style>
</head>
<body>
<div class="abs logo"><span class="logo-dot"></span><span class="logo-name">Tovrel Aquaculture Ltd</span></div>

<div class="abs contact">
  <div class="contact-top">hello@tovrel.com &nbsp;<b>Fax:</b> 604-555-0148</div>
  <div class="contact-call">
    <span class="phone-ico"><svg width="18" height="18" viewBox="0 0 24 24"><path fill="#fff" d="M6.6 10.8a15.1 15.1 0 0 0 6.6 6.6l2.2-2.2c.3-.3.7-.4 1-.2 1.1.4 2.3.6 3.6.6.6 0 1 .4 1 1V20c0 .6-.4 1-1 1A17 17 0 0 1 3 4c0-.6.4-1 1-1h3.5c.6 0 1 .4 1 1 0 1.3.2 2.5.6 3.6.1.3 0 .7-.2 1z"/></svg></span>
    <span class="label">CALL US TOLL-FREE ON</span><span class="num">1800 555 274</span>
  </div>
</div>

<div class="abs hero" role="img" aria-label="Aerial photo of forested hills and islands over a turquoise bay"></div>
<svg class="abs arrow" style="left:30px" width="40" height="96" viewBox="0 0 40 96"><polyline points="34,2 6,48 34,94" fill="none" stroke="rgba(40,70,90,.5)" stroke-width="5"/></svg>
<svg class="abs arrow" style="left:1132px" width="40" height="96" viewBox="0 0 40 96"><polyline points="6,2 34,48 6,94" fill="none" stroke="rgba(150,170,175,.8)" stroke-width="5"/></svg>

<nav class="abs nav">
  <a class="home" href="#">Home</a>
  <a href="#" style="width:172px">The&nbsp; Tovrel Story</a>
  <a href="#" style="width:248px">Mussel Powder Specifications</a>
  <a href="#" style="width:212px">Background Information</a>
  <a href="#" style="width:127px">Contact Us</a>
  <a href="#" style="width:108px">Site Map</a>
</nav>

<div class="abs below"></div>

<section class="abs intro">
  <h1>Tovrel Aquaculture Ltd</h1>
  <p>simply dummy text of the printing and typesetting industry. Lorem Ipsum has been the industry's standard dummy text ever since the 1500s, when an unknown printer took a galley of type and scrambled it to make a type specimen book. It has survived not only five centuries, but also the leap into electronic typesetting, remaining essentially unchanged. It was popularised in the 1960s with the release of Letraset sheets containing Lorem Ipsum passages, and more recently with desktop publishing software like Aldus PageMaker including versions of Lorem Ipsum.</p>
</section>
<a class="abs more">More Information <svg width="14" height="18" viewBox="0 0 14 18"><polyline points="3,2 11,9 3,16" fill="none" stroke="#777" stroke-width="2"/></svg></a>

<footer class="abs footer">
  <div class="abs foot-col" style="left:132px;top:22px"><h3>CATEGORIES</h3><ul><li>Did You Know?</li><li>Tovrel Aquaculture Ltd</li><li>60 Second Lessons</li><li>Recommend</li><li>About</li></ul></div>
  <div class="abs foot-col" style="left:358px;top:22px"><h3>POLICIES</h3><ul><li>Privacy Policy</li><li>Affiliate Disclaimer</li><li>Copyright</li><li>External Link Policy</li><li>Anti Spam Policy</li><li>DCMA Disclaimer</li></ul></div>
  <div class="abs foot-col" style="left:559px;top:22px"><h3>ADDRESS</h3><ul><li>418 Harbour Lane</li><li>Suite 210</li><li>Nelson, NZ 7010</li></ul></div>
</footer>
<div class="abs map" role="img" aria-label="Map of the coastline and islands near the company location"></div>

<div class="abs bottom">
  <span>Home</span><span>|</span><span>The&nbsp; Tovrel Story</span><span>|</span><span>Mussel Powder Specifications</span><span>|</span><span>Background Information</span><span>|</span><span>Contact Us</span><span>|</span><span>Site Map</span>
</div>
</body>
</html>
```